Banner to celebrate Pellister Journeys 40 years in business. Will be used on our social media channels.

Hello
We would like a banner created to celebrate 40 years in business with tagline "service through experience since 1983"
also add our website pellisterjourneys.com.au
Banner size must be : 650 x 150px
open to suggestions

Target Market(s)

current and prospective clients

Industry/Entity Type

Travel & Tourism (Business Travel)

Colors
0054AA
0677BA
7BADD7
CADEEF
E8F1F8

Requirements
Must have
• use current theme of our website www.pellisterjourneys.com.au. Keep simple and effective.
Nice to have
• use one image that I have provided
Should not have
• multiple graphics

```html
<!DOCTYPE html>
<html lang="en">
<head>
<meta charset="utf-8">
<title>Pellister Journeys – 40 Years Banners</title>
<link rel="stylesheet" href="https://fonts.googleapis.com/css2?family=Poppins:wght@400&family=Oswald:wght@500;600;700&family=Roboto:wght@500;700&display=swap">
<style>
  :root {
    --board-bg: #2468a5;
    --board-glow: #2f7ab8;
    --navy: #0b1e45;
    --brand-blue: #2a88d8;
    --logo-navy: #1f3f7a;
    --ribbon: #e8562a;
    --ink: #1a1a1a;
    --white: #ffffff;
  }
  * { margin: 0; padding: 0; box-sizing: border-box; }
  html, body { width: 1200px; height: 1200px; overflow: hidden; }
  body {
    background: radial-gradient(circle at 50% 50%, var(--board-glow) 0%, var(--board-bg) 70%);
    position: relative;
    font-family: "Roboto", Arial, sans-serif;
  }
  .board-label {
    position: absolute; left: 0; width: 1200px; text-align: center;
    font-family: "Poppins", sans-serif; font-size: 23px; color: var(--white);
    letter-spacing: 0.5px;
  }
  .banner {
    position: absolute; width: 650px; height: 150px;
    transform: scale(1.3333); transform-origin: 0 0;
    background: var(--white); overflow: hidden;
    box-shadow: 0 12px 30px rgba(0,0,0,0.35);
  }
  .banner-confetti {
    position: absolute; left: 0; top: 0; width: 200px; height: 150px;
    background: radial-gradient(circle at 50% 45%, #f3ead6 0%, rgba(255,255,255,0) 60%);
  }
  .banner-shapes { position: absolute; left: 0; top: 0; }
  .brand-name {
    position: absolute; left: 12px; top: 22px;
    font-family: "Roboto", sans-serif; font-weight: 700; font-size: 17px; line-height: 1;
    color: var(--logo-navy);
  }
  .visit-button {
    position: absolute; left: 6px; top: 91px; width: 59px; height: 22px;
    border-radius: 11px; background: var(--brand-blue); color: var(--white);
    font-family: "Oswald", sans-serif; font-weight: 600; font-size: 13px;
    display: flex; align-items: center; justify-content: center;
  }
  .visit-arrow { position: absolute; left: 68px; top: 95px; }
  .website {
    position: absolute; left: 7px; top: 122px; display: flex; align-items: center; gap: 4px;
    font-family: "Roboto", sans-serif; font-weight: 500; font-size: 10.5px; line-height: 14px; color: var(--ink);
  }
  .celebrate-text { font-family: "Oswald", sans-serif; font-weight: 600; font-size: 15px; fill: var(--white); }
  .number-text { font-family: "Oswald", sans-serif; font-weight: 700; font-size: 86px; fill: var(--white); }
  .ribbon-text { font-family: "Oswald", sans-serif; font-weight: 600; font-size: 11px; fill: var(--white); }
  .tagline-text { font-family: "Oswald", sans-serif; font-weight: 500; font-size: 12px; fill: var(--white); }
  .tagline-text .year { fill: var(--brand-blue); }
  .banner--two .tagline-text, .banner--three .tagline-text { font-style: italic; }
</style>
</head>
<body>

<p class="board-label" style="top:102px">BANNER-1 (650X150)</p>
<p class="board-label" style="top:449px">BANNER-2 (650X150)</p>
<p class="board-label" style="top:794px">BANNER-3 (650X150)</p>

<!-- Banner 1 -->
<section class="banner banner--one" style="left:175px; top:169px">
  <div class="banner-confetti"></div>
  <svg class="banner-shapes" width="650" height="150" viewBox="0 0 650 150">
    <defs>
      <linearGradient id="photo-one" x1="0" x2="1">
        <stop offset="0" stop-color="#c9c4bb"/><stop offset="0.6" stop-color="#8a6a4e"/><stop offset="1" stop-color="#d8d4cc"/>
      </linearGradient>
    </defs>
    <rect x="450" y="0" width="200" height="150" fill="url(#photo-one)" role="img" aria-label="Photo: traveller walking through an airport terminal with a suitcase"/>
    <circle cx="345" cy="150" r="160" fill="var(--brand-blue)"/>
    <circle cx="314" cy="132" r="129" fill="var(--navy)"/>
    <text class="celebrate-text" x="312" y="38" text-anchor="middle">CELEBRATE</text>
    <text class="number-text" x="309" y="117" text-anchor="middle">40</text>
    <g transform="rotate(12 339 80)"><polygon points="316,71 356,71 363,80 356,89 316,89" fill="var(--ribbon)"/><text class="ribbon-text" x="337" y="84.5" text-anchor="middle">YEARS</text></g>
    <text class="tagline-text" x="315" y="138" text-anchor="middle" textLength="229" lengthAdjust="spacingAndGlyphs">SERVICE THROUGH EXPERIENCE SINCE 1983</text>
  </svg>
  <div class="brand-name">Pellister Journeys</div>
  <div class="visit-button">VISIT</div>
  <svg class="visit-arrow" width="26" height="20" viewBox="0 0 26 20"><path d="M2 3 Q6 15 20 14" fill="none" stroke="var(--brand-blue)" stroke-width="1.5"/><path d="M16 10 L21 14 L16 18" fill="none" stroke="var(--brand-blue)" stroke-width="1.5"/></svg>
  <div class="website"><svg width="12" height="12" viewBox="0 0 12 12"><circle cx="6" cy="6" r="5" fill="none" stroke="#333"/><ellipse cx="6" cy="6" rx="2.2" ry="5" fill="none" stroke="#333"/><line x1="1" y1="6" x2="11" y2="6" stroke="#333"/></svg>www.pellisterjourneys.com.au</div>
</section>

<!-- Banner 2 -->
<section class="banner banner--two" style="left:167px; top:513px">
  <div class="banner-confetti"></div>
  <svg class="banner-shapes" width="650" height="150" viewBox="0 0 650 150">
    <defs>
      <linearGradient id="photo-two" x1="0" x2="1">
        <stop offset="0" stop-color="#b9c7cc"/><stop offset="0.55" stop-color="#8d9b98"/><stop offset="1" stop-color="#c6cbc9"/>
      </linearGradient>
    </defs>
    <rect x="440" y="0" width="210" height="150" fill="url(#photo-two)" role="img" aria-label="Photo: smiling businesswoman checking her phone at an airport"/>
    <circle cx="345" cy="150" r="160" fill="var(--brand-blue)"/>
    <circle cx="314" cy="132" r="129" fill="var(--navy)"/>
    <text class="celebrate-text" x="312" y="38" text-anchor="middle">CELEBRATE</text>
    <text class="number-text" x="309" y="117" text-anchor="middle">40</text>
    <g transform="rotate(12 339 80)"><polygon points="316,71 356,71 363,80 356,89 316,89" fill="var(--ribbon)"/><text class="ribbon-text" x="337" y="84.5" text-anchor="middle" font-style="italic">YEARS</text></g>
    <text class="tagline-text" x="315" y="138" text-anchor="middle" textLength="210" lengthAdjust="spacingAndGlyphs">SERVICE THROUGH EXPERIENCE SINCE <tspan class="year">1983</tspan></text>
  </svg>
  <div class="brand-name">Pellister Journeys</div>
  <div class="visit-button">VISIT</div>
  <svg class="visit-arrow" width="26" height="20" viewBox="0 0 26 20"><path d="M2 3 Q6 15 20 14" fill="none" stroke="var(--brand-blue)" stroke-width="1.5"/><path d="M16 10 L21 14 L16 18" fill="none" stroke="var(--brand-blue)" stroke-width="1.5"/></svg>
  <div class="website"><svg width="12" height="12" viewBox="0 0 12 12"><circle cx="6" cy="6" r="5" fill="none" stroke="#333"/><ellipse cx="6" cy="6" rx="2.2" ry="5" fill="none" stroke="#333"/><line x1="1" y1="6" x2="11" y2="6" stroke="#333"/></svg>www.pellisterjourneys.com.au</div>
</section>

<!-- Banner 3 -->
<section class="banner banner--three" style="left:167px; top:872px">
  <div class="banner-confetti"></div>
  <svg class="banner-shapes" width="650" height="150" viewBox="0 0 650 150">
    <defs>
      <linearGradient id="photo-three" x1="0" x2="1">
        <stop offset="0" stop-color="#e6e4e0"/><stop offset="0.5" stop-color="#b99a82"/><stop offset="1" stop-color="#6f7f90"/>
      </linearGradient>
    </defs>
    <rect x="450" y="0" width="200" height="150" fill="url(#photo-three)" role="img" aria-label="Photo: cheerful colleagues working together at a computer in an office"/>
    <circle cx="345" cy="150" r="160" fill="var(--brand-blue)"/>
    <circle cx="314" cy="132" r="129" fill="var(--navy)"/>
    <text class="celebrate-text" x="312" y="38" text-anchor="middle">CELEBRATE</text>
    <text class="number-text" x="309" y="117" text-anchor="middle">40</text>
    <g transform="rotate(12 339 80)"><polygon points="316,71 356,71 363,80 356,89 316,89" fill="var(--ribbon)"/><text class="ribbon-text" x="337" y="84.5" text-anchor="middle" font-style="italic">YEARS</text></g>
    <text class="tagline-text" x="315" y="138" text-anchor="middle" textLength="210" lengthAdjust="spacingAndGlyphs">SERVICE THROUGH EXPERIENCE SINCE <tspan class="year">1983</tspan></text>
  </svg>
  <div class="brand-name">Pellister Journeys</div>
  <div class="visit-button">VISIT</div>
  <svg class="visit-arrow" width="26" height="20" viewBox="0 0 26 20"><path d="M2 3 Q6 15 20 14" fill="none" stroke="var(--brand-blue)" stroke-width="1.5"/><path d="M16 10 L21 14 L16 18" fill="none" stroke="var(--brand-blue)" stroke-width="1.5"/></svg>
  <div class="website"><svg width="12" height="12" viewBox="0 0 12 12"><circle cx="6" cy="6" r="5" fill="none" stroke="#333"/><ellipse cx="6" cy="6" rx="2.2" ry="5" fill="none" stroke="#333"/><line x1="1" y1="6" x2="11" y2="6" stroke="#333"/></svg>www.pellisterjourneys.com.au</div>
</section>

</body>
</html>
```